Most captivating card ever!

Life Coach - Professional Adventurer - Entrepreneur
I need the worlds most amazing business card for my personal brand. This business card will mostly be used to give to prospective clients for life coaching and business coaching.
Be creative, be adventurous. It needs to stand out. Make people say.. I need this guy!
My background is as an entrepreneur and professional adventurer undertaking extreme expeditions. I am now moving into life coaching.
No specific design ideas, so you have full creativity. Show me your best.
Industry/Entity Type
Life Coaching
Contact Information for Business Card
Dan Pellow
itsdanp.com.au
0468215903
Colors
Designer to choose colors to be used in the design.
Look and feel

```html
<!DOCTYPE html>
<html lang="en">
<head>
<meta charset="utf-8">
<title>Dan Pellow – Business Card</title>
<link rel="stylesheet" href="https://fonts.googleapis.com/css2?family=Oswald:wght@400;500;600&display=swap">
<style>
  :root {
    --backdrop: #e4e4e4;
    --card: #ffffff;
    --ink: #111111;
    --ink-soft: #5a5a5a;
    --card-shadow: rgba(0, 0, 0, 0.14);
  }
  html, body {
    margin: 0;
    width: 1200px;
    height: 1000px;
    overflow: hidden;
    background: var(--backdrop);
  }
  .canvas {
    width: 1200px;
    height: 1000px;
    display: flex;
    align-items: center;
    justify-content: center;
  }
  .business-card {
    width: 900px;
    height: 550px;
    background: var(--card);
    box-shadow: 0 12px 40px var(--card-shadow);
    display: flex;
    flex-direction: column;
    align-items: center;
    justify-content: center;
    font-family: "Oswald", "Arial Narrow", sans-serif;
    text-transform: uppercase;
  }
  .card-name {
    margin: 0;
    font-size: 54px;
    font-weight: 600;
    letter-spacing: 0.12em;
    color: var(--ink);
    line-height: 1;
  }
  .card-roles {
    margin: 34px 0 0;
    font-size: 17px;
    font-weight: 600;
    letter-spacing: 0.1em;
    color: var(--ink);
  }
  .card-contact {
    margin: 30px 0 0;
    font-size: 30px;
    font-weight: 500;
    letter-spacing: 0.1em;
    color: var(--ink-soft);
  }
  .card-contact .divider {
    margin: 0 0.5em;
    font-weight: 400;
  }
</style>
</head>
<body>
  <main class="canvas">
    <section class="business-card">
      <h1 class="card-name">Dan Pellow</h1>
      <p class="card-roles">Life Coach - Professional Adventurer - Entrepreneur</p>
      <p class="card-contact">
        <span class="card-web">www.itsdanp.com.au</span><span class="divider">/</span><span class="card-phone">0468215903</span>
      </p>
    </section>
  </main>
</body>
</html>
```